Lidia Vanta Catering
Complete Stationery Design
Lidia Vanta Catering - Chef / Catering
Creative Brief
Bright & Fun-filled
Corazon Belmiro
Director, Sales & Marketing
2nd Floor, Quintero Bldg., Saldivar Avenue near corner Lupine Street, Navotas, Metro Manila, Philippines 1490
cbelmiro@lidiavanta-example.ph
www.lidiavanta-example.ph
Lidia Vanta is a high end catering company. Our design is modern Victorian. Color dark red, black and white but we are open to other color suggestion. We need the ff: - business cards - A4 and letter size paper with matching letter envelopes - Folder that fits A4 and letter size envelop - Fax Cover - CD sticker and cover - Sticker label - Address Sticker Label - Paper Bag Design - Styro lunch box design - Tissue Napkin Design - Name Plate - Identification Card Design
Victorian design with our Logo in the middle

```html
<!DOCTYPE html>
<html lang="en">
<head>
<meta charset="utf-8">
<title>Lidia Vanta Catering – Business Cards</title>
<link href="https://fonts.googleapis.com/css2?family=Arimo:wght@400;700&display=swap" rel="stylesheet">
<style>
  :root {
    --bg: #ece9e4;
    --brand-red: #cc0f1b;
    --ink-black: #141414;
    --paper: #ffffff;
    --logo-ink: #2a2a2a;
  }
  html, body {
    margin: 0;
    padding: 0;
    width: 1200px;
    height: 852px;
    overflow: hidden;
    background: var(--bg);
    font-family: "Arimo", Arial, sans-serif;
  }
  .canvas {
    position: relative;
    width: 1200px;
    height: 852px;
  }
  .card {
    position: absolute;
    width: 520px;
    height: 300px;
    border-radius: 22px;
    overflow: hidden;
    box-shadow: 0 6px 18px rgba(0,0,0,0.18);
    background: var(--brand-red);
  }
  .card--front { left: 70px; top: 110px; }
  .card--reverse { left: 610px; top: 440px; }
  .card-shape {
    position: absolute;
    inset: 0;
    width: 100%;
    height: 100%;
  }
  .card--reverse .card-shape { transform: scaleX(-1); }
  .card-shape .paper { fill: var(--paper); }
  .card-shape .edge { fill: var(--ink-black); }

  .contact {
    position: absolute;
    top: 44px;
    color: var(--paper);
    font-size: 12.5px;
    line-height: 1.42;
  }
  .card--front .contact { left: 28px; text-align: left; }
  .card--reverse .contact { right: 28px; text-align: right; }
  .contact .name {
    font-weight: 700;
    font-size: 15px;
    margin: 0;
  }
  .contact .title {
    font-weight: 700;
    font-size: 11px;
    margin: 0 0 34px;
  }
  .contact .address { margin: 0 0 6px; }
  .contact .line {
    display: flex;
    align-items: center;
    gap: 7px;
    margin: 0;
  }
  .card--reverse .contact .line { justify-content: flex-end; }
  .icon { width: 12px; height: 12px; fill: var(--paper); flex: none; }

  .brand {
    position: absolute;
    top: 0;
    bottom: 0;
    width: 280px;
    display: flex;
    flex-direction: column;
    align-items: center;
    justify-content: center;
    color: var(--logo-ink);
  }
  .card--front .brand { right: 10px; }
  .card--reverse .brand { left: 10px; }
  .brand-name {
    font-size: 30px;
    font-weight: 400;
    margin: 0;
    letter-spacing: 0.5px;
  }
  .brand-tag {
    font-size: 11px;
    font-weight: 400;
    letter-spacing: 2.5px;
    text-transform: uppercase;
    margin: 6px 0 0;
  }
</style>
</head>
<body>
<main class="canvas">

  <section class="card card--front" aria-label="Business card, front">
    <svg class="card-shape" viewBox="0 0 520 300" aria-hidden="true">
      <path class="edge" d="M262 0 C212 90 212 210 262 300 L270 300 C222 210 222 90 270 0 Z"/>
      <path class="paper" d="M268 0 C220 90 220 210 268 300 L520 300 L520 0 Z"/>
    </svg>
    <div class="contact">
      <p class="name">Corazon Belmiro</p>
      <p class="title">Director, Sales &amp; Marketing</p>
      <p class="address">2nd Floor, Quintero Bldg.,<br>Saldivar Avenue<br>Near corner Lupine Street<br>Navotas, Metro Manila<br>Philippines 1490</p>
      <p class="line"><svg class="icon" viewBox="0 0 12 12"><path d="M2 1h3l1 3-1.5 1a7 7 0 0 0 2.5 2.5L8 6l3 1v3c0 .6-.4 1-1 1A9 9 0 0 1 1 2c0-.6.4-1 1-1z"/></svg>+632 555 0148</p>
      <p class="line"><svg class="icon" viewBox="0 0 12 12"><rect x="3" y="0.5" width="6" height="11" rx="1"/></svg>+63917 555 0192</p>
      <p class="line"><svg class="icon" viewBox="0 0 12 12"><circle cx="6" cy="6" r="5.5"/></svg>cbelmiro@lidiavanta-example.ph</p>
      <p class="line"><svg class="icon" viewBox="0 0 12 12"><circle cx="6" cy="6" r="5.5"/></svg>www.lidiavanta-example.ph</p>
    </div>
    <div class="brand">
      <p class="brand-name">Lidia Vanta</p>
      <p class="brand-tag">Catering</p>
    </div>
  </section>

  <section class="card card--reverse" aria-label="Business card, reverse layout">
    <svg class="card-shape" viewBox="0 0 520 300" aria-hidden="true">
      <path class="edge" d="M262 0 C212 90 212 210 262 300 L270 300 C222 210 222 90 270 0 Z"/>
      <path class="paper" d="M268 0 C220 90 220 210 268 300 L520 300 L520 0 Z"/>
    </svg>
    <div class="brand">
      <p class="brand-name">Lidia Vanta</p>
      <p class="brand-tag">Catering</p>
    </div>
    <div class="contact">
      <p class="name">Corazon Belmiro</p>
      <p class="title">Director, Sales &amp; Marketing</p>
      <p class="address">2nd Floor, Quintero Bldg.,<br>Saldivar Avenue<br>Near corner Lupine Street<br>Navotas, Metro Manila<br>Philippines 1490</p>
      <p class="line">+632 555 0148<svg class="icon" viewBox="0 0 12 12"><path d="M2 1h3l1 3-1.5 1a7 7 0 0 0 2.5 2.5L8 6l3 1v3c0 .6-.4 1-1 1A9 9 0 0 1 1 2c0-.6.4-1 1-1z"/></svg></p>
      <p class="line">+63917 555 0192<svg class="icon" viewBox="0 0 12 12"><rect x="3" y="0.5" width="6" height="11" rx="1"/></svg></p>
      <p class="line">cbelmiro@lidiavanta-example.ph<svg class="icon" viewBox="0 0 12 12"><circle cx="6" cy="6" r="5.5"/></svg></p>
      <p class="line">www.lidiavanta-example.ph<svg class="icon" viewBox="0 0 12 12"><circle cx="6" cy="6" r="5.5"/></svg></p>
    </div>
  </section>

</main>
</body>
</html>
```